Musician Business Card Design

I am freelance Double Bass player based in New York. I play every style of music, from Pop music to Contemporary Classical Music. I am also a private Bass and music theory teacher. What I hope to communicate with my business card is that I am a reliable and competent musician. I like designs with geometric patterns, I am very found of mandalas, so maybe we could incorporate that into the idea. I am looking for a design that will be easy on the eyes, and will have something that will make people want to keep it.
Thanks for all your help.

Industry/Entity Type

Business

Contact Information for Business Card

Tomas Verrault
+1 (347) 555-0182
okafor.tm@quillnest.com

```html
<!DOCTYPE html>
<html lang="en">
<head>
<meta charset="utf-8">
<title>Tomas Verrault – Business Card</title>
<link rel="stylesheet" href="https://fonts.googleapis.com/css2?family=Lato:wght@300;400;700&display=swap">
<style>
  :root {
    --canvas-bg: #ecebe9;
    --card-dark: #353535;
    --card-light: #ffffff;
    --accent-red: #e8424e;
    --text-grey: #6e6e6e;
    --text-soft: #8a8a8a;
    --pattern-grey: #cfcfcf;
    --pattern-dark: #5a5a5a;
    --pattern-pink: #f6c2bd;
    --icon-ring: #d9d9d9;
  }
  * { box-sizing: border-box; margin: 0; padding: 0; }
  html, body { width: 1200px; height: 780px; overflow: hidden; }
  body {
    background: var(--canvas-bg);
    font-family: "Lato", Arial, sans-serif;
    position: relative;
  }
  .card {
    position: absolute;
    top: 247px;
    width: 500px;
    height: 286px;
    overflow: hidden;
    box-shadow: 0 6px 18px rgba(0,0,0,0.18);
  }

  /* Back side */
  .card--back { left: 70px; background: var(--card-dark); }
  .card--back .pattern {
    position: absolute;
    right: 0; top: 0;
    width: 330px; height: 180px;
    background: radial-gradient(ellipse at 80% 10%, var(--pattern-dark) 0%, rgba(90,90,90,0.45) 45%, rgba(53,53,53,0) 75%);
  }
  .card--back .lockup {
    position: absolute;
    left: 40px; bottom: 56px;
    display: flex; align-items: center; gap: 14px;
  }
  .card--back .lockup-dot {
    width: 16px; height: 16px; border-radius: 50%;
    border: 2px solid var(--accent-red);
  }
  .card--back .lockup-name {
    color: #ffffff;
    font-size: 30px;
    font-weight: 400;
    letter-spacing: 1px;
  }

  /* Front side */
  .card--front { left: 630px; background: var(--card-light); }
  .card--front .pattern-right {
    position: absolute;
    right: 0; top: 0;
    width: 240px; height: 286px;
    background: radial-gradient(ellipse at 85% 50%, #e4e4e4 0%, rgba(228,228,228,0.5) 45%, rgba(255,255,255,0) 78%);
  }
  .card--front .pattern-left {
    position: absolute;
    left: 0; bottom: 0;
    width: 140px; height: 200px;
    background: radial-gradient(ellipse at 10% 75%, var(--pattern-pink) 0%, rgba(246,194,189,0.4) 45%, rgba(255,255,255,0) 78%);
  }
  .name {
    position: absolute;
    left: 48px; top: 50px;
    font-size: 26px;
    font-weight: 700;
    color: var(--text-grey);
  }
  .name .surname { color: var(--accent-red); font-weight: 400; }
  .contact-list {
    position: absolute;
    left: 48px; top: 108px;
    list-style: none;
  }
  .contact-item {
    display: flex; align-items: center; gap: 12px;
    font-size: 13px;
    color: var(--text-soft);
    margin-bottom: 16px;
  }
  .contact-icon {
    width: 24px; height: 24px;
    border-radius: 50%;
    border: 1px solid var(--icon-ring);
    display: flex; align-items: center; justify-content: center;
  }
</style>
</head>
<body>

  <section class="card card--back" aria-label="Card back">
    <div class="pattern" role="img" aria-label="Geometric network pattern of connected lines and dots"></div>
    <div class="lockup">
      <span class="lockup-dot"></span>
      <span class="lockup-name">TOMAS VERRAULT</span>
    </div>
  </section>

  <section class="card card--front" aria-label="Card front">
    <div class="pattern-right" role="img" aria-label="Light grey geometric network pattern"></div>
    <div class="pattern-left" role="img" aria-label="Soft pink geometric network pattern"></div>
    <h1 class="name">Tomas <span class="surname">Verrault</span></h1>
    <ul class="contact-list">
      <li class="contact-item">
        <span class="contact-icon">
          <svg width="12" height="12" viewBox="0 0 12 12" aria-hidden="true">
            <path d="M3 1.5 L4.8 1.5 L5.4 3.8 L4.2 4.8 C4.9 6.2 5.8 7.1 7.2 7.8 L8.2 6.6 L10.5 7.2 L10.5 9 C10.5 9.8 9.8 10.5 9 10.5 C5.2 10.2 1.8 6.8 1.5 3 C1.5 2.2 2.2 1.5 3 1.5 Z" fill="var(--accent-red)"/>
          </svg>
        </span>
        <span>+1 (347) 555-0182</span>
      </li>
      <li class="contact-item">
        <span class="contact-icon">
          <svg width="12" height="12" viewBox="0 0 12 12" aria-hidden="true">
            <rect x="1" y="2.5" width="10" height="7" rx="1" fill="var(--accent-red)"/>
            <path d="M1.5 3 L6 6.5 L10.5 3" fill="none" stroke="#ffffff" stroke-width="1"/>
          </svg>
        </span>
        <span>okafor.tm@quillnest.com</span>
      </li>
    </ul>
  </section>

</body>
</html>
```